Roll-up Banner für Wolkenwerkstatt
Zielgruppe
Wir, die Norddeutscher Verband für Heitere Seelenkunde, widmen uns der Aus- und Fortbildung im Bereich der Positiven Psychologie. Wir bilden Coaches, Trainer, Berater, Therapeuten, Pädagogen und Führungskräfte darin aus, wie sie Ihren Klienten helfen können ein erfüllteres und glücklicheres Leben zu gestalten.
Wir arbeiten zusammen mit verschiedenen Universitäten, Forschern und Wissenschaftlern und ermöglichen so den Brückenschlag zwischen Wissenschaft und der praktischen Arbeit mit Klienten.
Wir zeichnen uns durch die Kombination von hoher Professionalität und großer menschlicher Wärme und Verbundenheit aus.
Unser Ziel ist es durch Wissensvermittlung einen gesellschaftlichen Unterschied zu machen. Der Mensch steht für uns im Mittelpunkt.
Unsere Zielgruppe sind Coaches, Trainer, Berater, Therapeuten, Pädagogen und Führungskräfte.
Aufgabenstellung
Das Banner soll als Rollup-Banner (1x2m) fungieren und uns bei Kongressen und Tagungen repräsentieren. Es muss von weitem gut erkennbar sein. Unser Logo sollte in irgendeiner Form enthalten sein eventuell auch nur Teile als grafische Einbindung. Der Firmenname Norddeutscher Verband für Heitere Seelenkunde, muss gut erkennbar sein. Die website nvhs-portal.example sollte gut sichtbar Teil des Entwurfes sein.
Bei der Einbindung von Bildern sollten Sie beachten, dass wir eine sehr heterogene Zielgruppe haben, sich also Pädagogen ebenso wiederfinden müssen wie Führungskräfte, Männer, wie Frauen. Ansonsten könnte auch eine grafische Lösung oder Bilder ohne Personen genutzt werden.
Wir haben Ihnen einige Beispiele für andere Werbematerialien von uns angehangen. Es wäre wichtig, dass das Banner zu diesem Corporate Design passt.
HINWEIS: Da wir das Banner bereits Ende nächster Woche einsetzen wollen, küren wir bereits am Montagmorgen (den 17.9.2018) den Sieger.

```html
<!DOCTYPE html>
<html lang="de">
<head>
<meta charset="utf-8">
<title>Roll-up Banner – Norddeutscher Verband für Heitere Seelenkunde</title>
<link rel="stylesheet" href="https://fonts.googleapis.com/css2?family=PT+Sans:wght@400;700&family=PT+Sans+Narrow:wght@400;700&family=Crimson+Pro:wght@400&display=swap">
<style>
  :root {
    --stage: #d9dade;
    --white: #ffffff;
    --navy: #0c2d5c;
    --green: #6cb955;
    --mid: #16a98a;
    --teal: #00b3c4;
    --board: #333333;
    --board-dark: #262626;
    --rule: #0c2d5c;
    --partner: #4a4f5c;
  }
  * { box-sizing: border-box; margin: 0; padding: 0; }
  html, body { width: 1200px; height: 1200px; overflow: hidden; background: var(--stage); }
  .banner {
    position: absolute; left: 305px; top: 0;
    width: 590px; height: 1200px;
    background: var(--white);
    font-family: "PT Sans", sans-serif;
  }
  .header { position: absolute; left: 0; top: 0; width: 590px; height: 190px; }
  .brand { position: absolute; left: 72px; top: 96px; display: flex; align-items: center; gap: 8px; }
  .brand-dot { width: 14px; height: 14px; border-radius: 50%; background: var(--teal); }
  .brand-name { font-family: "PT Sans", sans-serif; font-weight: 700; font-size: 22px; letter-spacing: 1px; color: var(--navy); }
  .brand-full { position: absolute; left: 72px; top: 146px; width: 150px; font-size: 9px; line-height: 12px; color: var(--navy); }
  .brand-full strong { font-weight: 700; }
  .url {
    position: absolute; right: 35px; top: 80px;
    font-family: "PT Sans", sans-serif; font-weight: 700; font-size: 31px; color: var(--navy);
    letter-spacing: -0.3px;
  }
  .photo { position: absolute; left: 0; top: 190px; width: 590px; height: 326px; }
  .feature {
    position: absolute; left: 0; top: 516px; width: 590px; height: 518px;
    background: linear-gradient(90deg, var(--green) 0%, var(--mid) 50%, var(--teal) 100%);
    color: var(--white);
  }
  .feature-rule { position: absolute; left: 0; top: 1034px; width: 590px; height: 4px; background: var(--rule); }
  .intro {
    position: absolute; left: 30px; top: 36px; width: 177px;
    font-family: "PT Sans Narrow", sans-serif; font-size: 11px; line-height: 15.2px; text-align: right;
  }
  .intro p + p { margin-top: 15px; }
  .intro strong { font-weight: 700; }
  .divider { position: absolute; left: 224px; top: 20px; width: 1px; height: 447px; background: var(--white); }
  .headline {
    position: absolute; left: 239px; top: 28px; width: 330px;
    font-weight: 700; font-size: 29px; line-height: 38px;
  }
  .quote-mark { position: absolute; left: 370px; font-family: "PT Sans", sans-serif; font-weight: 700; font-size: 60px; line-height: 1; }
  .quote-mark.open { top: 150px; }
  .quote-mark.close { top: 322px; }
  .quote {
    position: absolute; left: 239px; top: 202px; width: 330px;
    font-family: "Crimson Pro", serif; font-size: 29px; line-height: 38px;
  }
  .quote-author { position: absolute; left: 423px; top: 337px; font-weight: 700; font-size: 11px; letter-spacing: 0.2px; font-family: "PT Sans Narrow", sans-serif; }
  .footer { position: absolute; left: 0; top: 1038px; width: 590px; height: 162px; }
  .footer-title { position: absolute; left: 0; top: 20px; width: 590px; text-align: center; font-size: 11px; color: var(--navy); }
  .partners { position: absolute; left: 22px; top: 62px; width: 550px; display: flex; justify-content: space-between; align-items: center; }
  .partner { display: flex; align-items: center; gap: 6px; font-size: 11px; line-height: 13px; color: var(--partner); }
  .partner-mark { width: 12px; height: 12px; border-radius: 50%; background: var(--partner); flex: none; }
</style>
</head>
<body>
<main class="banner">
  <header class="header">
    <div class="brand"><span class="brand-dot"></span><span class="brand-name">NVHS</span></div>
    <div class="brand-full">Norddeutscher Verband für <strong>Heitere Seelenkunde</strong></div>
    <div class="url">NVHS-PORTAL.EXAMPLE</div>
  </header>

  <svg class="photo" viewBox="0 0 590 326" role="img" aria-label="Foto: Kreidezeichnung auf Tafel, ein trauriges Gesicht wird per Pfeil zu einem lachenden Gesicht, darunter blickt ein Mann mit Brille nach oben">
    <defs>
      <radialGradient id="boardGlow" cx="50%" cy="40%" r="70%">
        <stop offset="0%" stop-color="var(--board)"/>
        <stop offset="100%" stop-color="var(--board-dark)"/>
      </radialGradient>
    </defs>
    <rect width="590" height="326" fill="url(#boardGlow)"/>
  </svg>

  <section class="feature">
    <div class="intro">
      <p>Wir, der <strong>Norddeutsche Verband für Heitere Seelenkunde</strong>, widmen uns der <strong>Aus- und Fortbildung</strong> im Bereich der Positiven Psychologie. Wir bilden Coaches, Trainer, Berater, Therapeuten, Pädagogen und Führungskräfte darin aus, wie sie Ihren Klienten helfen können ein erfüllteres und glücklicheres Leben zu gestalten.</p>
      <p>Wir arbeiten zusammen mit verschiedenen Universitäten, Forschern und Wissenschaftlern und ermöglichen so den Brückenschlag zwischen Wissenschaft und der praktischen Arbeit mit Klienten.</p>
      <p>Unser Ziel ist es durch Wissensvermittlung einen gesellschaftlichen Unterschied zu machen. Der Mensch steht für uns im Mittelpunkt.</p>
    </div>
    <div class="divider"></div>
    <h1 class="headline">Zertifizierte Ausbildung Positive Bildung</h1>
    <div class="quote-mark open">”</div>
    <blockquote class="quote">Wenn wir anderen zum Glück verhelfen, werden wir selbst glücklich.</blockquote>
    <div class="quote-mark close">“</div>
    <div class="quote-author">MATHIS ROLLAND</div>
  </section>
  <div class="feature-rule"></div>

  <footer class="footer">
    <div class="footer-title">Forschungskooperationspartner:</div>
    <div class="partners">
      <div class="partner"><span class="partner-mark"></span>Hochschule<br>Lindenau</div>
      <div class="partner">Akademie Seeburg</div>
      <div class="partner">Universität Weidental</div>
      <div class="partner"><span class="partner-mark"></span>TECHNISCHE<br>HOCHSCHULE<br>BRUNNFELD</div>
    </div>
  </footer>
</main>
</body>
</html>
```